Creative Web design for Tattoo Artist

I am a tattoo artist with a private tattoo/art studio in Spring, TX. I need to design a website for my studio, to include the following "pages" :
-home/about
-FAQ
-Gallery
-Inquiries
-shop
We would like to see designs that are more dark or "moody", and like the colors black/gold.
I'd like my website to reflect my studio, an award winning private, upscale custom only tattoo studio.

I've attached some examples of styles we liked.

Target Market(s)

adults ages 18-50, interested in tattoos, or fine art

Industry/Entity Type

Tattoos/Fine Art/Arts

Coding

Coded - Design and coding required

Number of Pages Required

5+ page

Colors

Designer to choose colors to be used in the design.

Requirements
Must have
• gallery section, and e-commerce page set up so I can begin selling merchandise, I'd like the fonts to flow with my logo design

```html
<!DOCTYPE html>
<html lang="en">
<head>
<meta charset="utf-8">
<title>The Gilded Viper — Custom Tattoo Studio</title>
<link href="https://fonts.googleapis.com/css2?family=Cinzel:wght@400;500;600;700&family=Outfit:wght@300;400;500&display=swap" rel="stylesheet">
<style>
:root{
  --gold:#d4a00c;
  --ink:#0b0b0b;
  --slate:#1f1f1f;
  --field:#2a2a2a;
  --text:#ffffff;
}
*{margin:0;padding:0;box-sizing:border-box}
html,body{width:1200px;height:4172px;overflow:hidden;background:var(--ink);color:var(--text);font-family:'Outfit',sans-serif}
.page{position:relative;width:1200px;height:4172px}
section,footer{position:absolute;left:0;width:1200px;overflow:hidden}
.abs{position:absolute}
.photo{position:absolute}
.gold{color:var(--gold)}
.btn{position:absolute;background:var(--gold);color:#fff;font-family:'Cinzel',serif;font-size:11px;font-weight:600;display:flex;align-items:center;justify-content:center;letter-spacing:.3px}
.section-title{position:absolute;left:0;width:1200px;text-align:center;font-family:'Cinzel',serif;font-size:29px;font-weight:500;letter-spacing:.5px}
.ghost-num{position:absolute;left:0;width:1200px;text-align:center;font-family:'Cinzel',serif;font-size:150px;font-weight:700;color:rgba(255,255,255,.05);line-height:1}
.rule{position:absolute}

/* hero */
.hero{top:0;height:625px}
.hero .photo{inset:0;background:radial-gradient(ellipse at 55% 30%,#3a3028 0%,#1f1a16 40%,#0e0c0a 100%)}
.hero .shade{position:absolute;inset:0;background:linear-gradient(180deg,rgba(0,0,0,.25),rgba(0,0,0,.45))}
.nav a{position:absolute;top:48px;font-size:12px;color:#e8e8e8;text-decoration:none;letter-spacing:.3px}
.nav a.active{color:var(--gold)}
.nav .underline{position:absolute;left:152px;top:75px;width:62px;height:1px;background:var(--gold)}
.brand-mark{position:absolute;left:540px;top:10px;width:120px;height:96px;display:flex;flex-direction:column;align-items:center;justify-content:center;gap:6px}
.brand-mark .dot{width:26px;height:26px;border:2px solid #fff;border-radius:50%}
.brand-mark span{font-family:'Cinzel',serif;font-size:11px;font-weight:600;text-align:center;line-height:1.2;color:#fff}
.search{position:absolute;left:1002px;top:40px;width:32px;height:32px;border-radius:50%;background:var(--gold);display:flex;align-items:center;justify-content:center}
.hero .welcome{position:absolute;top:198px;left:0;width:1200px;text-align:center;font-family:'Cinzel',serif;font-size:25px;font-weight:500}
.hero h1{position:absolute;top:232px;left:0;width:1200px;text-align:center;font-family:'Cinzel',serif;font-size:68px;font-weight:600;line-height:68px;color:var(--gold);letter-spacing:.5px}
.hero p{position:absolute;top:426px;left:310px;width:580px;text-align:center;font-size:11px;font-style:italic;line-height:20px;color:#eee}

/* about */
.about{top:625px;height:350px;background:var(--ink)}
.about .photo{left:0;top:0;width:640px;height:350px;background:radial-gradient(ellipse at 30% 45%,#2c2520 0%,#15120f 55%,#0b0b0b 100%)}
.about h2{position:absolute;left:279px;top:105px;font-family:'Cinzel',serif;font-size:29px;font-weight:500;line-height:36px}
.about .copy{position:absolute;left:623px;top:44px;width:415px;font-size:10.3px;line-height:19.8px;color:#e4e4e4;text-align:justify}

/* shop */
.shop{top:975px;height:651px;background:var(--slate)}
.shop .photo{inset:0;background:radial-gradient(ellipse at 50% 70%,#2a2a2a 0%,#1c1c1c 60%,#161616 100%)}
.card{position:absolute;top:204px;width:246px}
.card .frame{position:absolute;width:226px;height:270px;border:1.5px solid #cfcfcf}
.card .frame.gold-frame{border:none;background:var(--gold)}
.card .img{position:absolute;left:0;top:0;width:246px;height:295px}
.card .cap{position:absolute;top:318px;left:-20px;width:286px;text-align:center;font-family:'Cinzel',serif;font-size:11.5px;line-height:19px;font-weight:500}
.card .price{position:absolute;top:357px;left:0;width:246px;text-align:center;font-size:12px;color:var(--gold)}

/* faq */
.faq{top:1626px;height:716px;background:#121212}
.faq .photo{inset:0;background:radial-gradient(ellipse at 30% 20%,#262626 0%,#141414 55%,#0e0e0e 100%)}
.row{position:absolute;left:254px;width:692px;height:39px;border-radius:20px;background:#2b2b2b;display:flex;align-items:center}
.row .num{width:31px;height:31px;margin-left:4px;border-radius:50%;background:#151515;font-size:11px;display:flex;align-items:center;justify-content:center}
.row.open .num{background:var(--gold)}
.row .q{margin-left:22px;font-family:'Cinzel',serif;font-size:11px;font-weight:500;flex:1}
.row .pm{width:40px;color:#777;font-size:16px}
.row.open .pm{color:var(--gold)}
.answer{position:absolute;left:310px;top:398px;width:590px;font-size:11px;line-height:19.8px;color:#ddd}

/* gallery */
.gallery{top:2342px;height:983px;background:#1a1a1a}
.gallery .photo.bg{inset:0;background:radial-gradient(ellipse at 70% 15%,#2a2a2a 0%,#1a1a1a 60%,#151515 100%)}
.tile{position:absolute}

/* contact */
.contact{top:3325px;height:481px;background:#0a0a0a}
.contact .photo{inset:0;background:radial-gradient(ellipse at 50% 10%,#1c1c1c 0%,#0a0a0a 70%)}
.field{position:absolute;width:256px;height:36px;background:var(--field);font-size:10px;color:#8c8c8c;padding:11px 9px}
.info{position:absolute;left:745px;display:flex;gap:14px}
.ico{width:40px;height:40px;border-radius:50%;background:var(--gold);display:flex;align-items:center;justify-content:center;flex:none}
.info h4{font-size:13px;font-weight:500;margin-top:1px}
.info p{font-size:13px;line-height:20px;margin-top:2px}

/* footer */
.footer{top:3806px;height:366px;background:#171717}
.foot-brand{position:absolute;left:160px;top:50px;width:95px;height:160px;display:flex;flex-direction:column;align-items:center;justify-content:center;gap:8px}
.foot-brand .dot{width:34px;height:34px;border:2px solid #fff;border-radius:50%}
.foot-brand span{font-family:'Cinzel',serif;font-size:13px;font-weight:600;text-align:center;line-height:1.25}
.fcol{position:absolute;top:48px}
.fcol h5{font-size:12px;font-weight:400;color:#fff}
.fcol h5 b{font-weight:400;color:var(--gold)}
.fcol ul{list-style:none;margin-top:14px}
.fcol li{font-size:11px;line-height:22px;display:flex;align-items:center;gap:9px}
.fcol li i{font-style:normal;color:var(--gold);font-size:10px}
.fcol li .sq{width:8px;height:8px;border-radius:50%;background:var(--gold)}
.fc-item{display:flex;gap:10px;margin-top:14px}
.fc-item .ico{width:30px;height:30px}
.fc-item h6{font-size:9.5px;font-weight:500}
.fc-item p{font-size:9.5px;line-height:15px}
.nl p{font-size:10.5px;line-height:19px;margin-top:12px;width:260px}
.nl .in{width:245px;border-bottom:1px solid #666;font-size:8.5px;color:#888;padding-bottom:10px;margin-top:18px}
</style>
</head>
<body>
<div class="page">

<section class="hero">
  <div class="photo" role="img" aria-label="Dim close-up of a tattoo artist working with a tattoo machine"></div>
  <div class="shade"></div>
  <nav class="nav">
    <a class="active" style="left:162px">HOME</a>
    <a style="left:245px">ABOUT</a>
    <a style="left:330px">FAQ</a>
    <a style="left:402px">GALLERY</a>
    <a style="left:759px">INQUIRIES</a>
    <a style="left:862px">SHOP</a>
    <div class="underline"></div>
  </nav>
  <div class="brand-mark"><div class="dot"></div><span>THE GILDED<br>VIPER</span></div>
  <div class="search"><svg width="12" height="12" viewBox="0 0 12 12"><circle cx="5" cy="5" r="3.6" fill="none" stroke="#fff" stroke-width="1.6"/><line x1="7.7" y1="7.7" x2="11" y2="11" stroke="#fff" stroke-width="1.6"/></svg></div>
  <div class="welcome">WELCOME TO THE GILDED VIPER</div>
  <h1>BRING YOUR SKIN BACK<br>TO LIFE</h1>
  <svg class="rule" style="left:282px;top:389px" width="630" height="16"><circle cx="9" cy="8" r="7" fill="#fff"/><path d="M9 6.5 L610 4 L630 6 L610 10 L9 9.5Z" fill="#fff"/></svg>
  <p>Lorem ipsum dolor sit amet, consectetur adipiscing elit, sed do eiusmod tempor incididunt ut labore et dolore magna aliqua sed do eiusmod tempor.</p>
  <div class="btn" style="left:528px;top:492px;width:143px;height:30px">GET STARTED</div>
  <svg class="abs" style="left:143px;top:538px" width="40" height="12"><path d="M40 6H2M8 1L2 6L8 11" stroke="#fff" fill="none" stroke-width="1.2"/></svg>
  <svg class="abs" style="left:1016px;top:538px" width="40" height="12"><path d="M0 6H38M32 1L38 6L32 11" stroke="#fff" fill="none" stroke-width="1.2"/></svg>
</section>

<section class="about">
  <div class="photo" role="img" aria-label="Tattoo machine resting in shadow"></div>
  <h2>ABOUT THE<br><span class="gold">GILDED VIPER</span></h2>
  <svg class="rule" style="left:279px;top:180px" width="283" height="10"><circle cx="5" cy="5" r="4.5" fill="#fff"/><path d="M5 4 L270 3.5 L283 4.5 L270 6.5 L5 6Z" fill="#fff"/></svg>
  <div class="btn" style="left:316px;top:228px;width:143px;height:31px">LEARN MORE</div>
  <p class="copy">Lorem ipsum dolor sit amet, consectetur adipiscing elit, sed do eiusmod tempor incididunt ut labore et dolore magna aliqua. Quis ipsum suspendisse ultrices gravida. Risus commodo viverra maecenas accumsan lacus vel facilisis. iste natus error sit voluptatem accusantium doloremque laudantium, totam rem aperiam, iste natus error sit voluptatem accusantium doloremque laudantium, totam rem aperiam, eaque ipsa quae ab illo inventore veritatis et quasi architecto.iste natus error sit voluptatem accusantium doloremque laudantium, totam rem aperiam, eaque ipsa quae ab illo inventore veritatis et quasi architecto beatae vitae dicta sunt explicabo. Nemo enim ipsam voluptatem quia voluptas sit aspernatur aut odit aut fugit, sed quia consequuntur magni dolores eos qui ratione voluptatem sequi nesciunt. Neque porro quisquam est, qui dolorem ipsum quia dolor sit ametexercitationem ullam corporis suscipit laboriosamommodi consequatur.</p>
</section>

<section class="shop">
  <div class="photo" role="img" aria-label="Faint tattoo machine parts in the background"></div>
  <div class="ghost-num" style="top:12px">02</div>
  <div class="section-title" style="top:80px">SHOP <span class="gold">OUR TATTOO</span></div>
  <svg class="rule" style="left:474px;top:120px" width="250" height="10"><circle cx="5" cy="5" r="4.5" fill="#fff"/><path d="M5 4 L238 3.5 L250 4.5 L238 6.5 L5 6Z" fill="#fff"/></svg>
  <svg class="abs" style="left:92px;top:343px" width="40" height="12"><path d="M40 6H2M8 1L2 6L8 11" stroke="#888" fill="none" stroke-width="1.2"/></svg>
  <svg class="abs" style="left:1068px;top:343px" width="40" height="12"><path d="M0 6H38M32 1L38 6L32 11" stroke="#fff" fill="none" stroke-width="1.2"/></svg>

  <div class="card" style="left:162px">
    <div class="frame" style="left:30px;top:-12px"></div>
    <div class="img photo" role="img" aria-label="Woman with floral sleeve tattoos on both arms" style="background:linear-gradient(160deg,#d9cfcb,#b79a94 55%,#6b5a58)"></div>
    <div class="cap">LOREM IPSUM DOLOR SIT AMET<br>CONSECTETUR ADIPISCING ELIT, SED DO</div>
    <div class="price">$ 120:00</div>
  </div>
  <div class="card" style="left:471px">
    <div class="frame gold-frame" style="left:30px;top:-12px"></div>
    <div class="img photo" role="img" aria-label="Man with full chest and arm tattoos" style="background:linear-gradient(170deg,#3a3a3a,#5c5148 55%,#2a2826)"></div>
    <div class="cap">LOREM IPSUM DOLOR SIT AMET<br>CONSECTETUR ADIPISCING ELIT, SED DO</div>
    <div class="price">$ 120:00</div>
  </div>
  <div class="card" style="left:780px">
    <div class="frame" style="left:30px;top:-12px"></div>
    <div class="img photo" role="img" aria-label="Back piece tattoo on a model against a dark backdrop" style="background:radial-gradient(ellipse at 50% 45%,#4a3a3a,#151a22 70%)"></div>
    <div class="cap">LOREM IPSUM DOLOR SIT AMET<br>CONSECTETUR ADIPISCING ELIT, SED DO</div>
    <div class="price">$ 120:00</div>
  </div>
</section>

<section class="faq">
  <div class="photo" role="img" aria-label="Dark blurred studio scene"></div>
  <div class="ghost-num" style="top:50px">03</div>
  <div class="section-title" style="top:120px">FREQUENTLY <span class="gold">ASKED QUESTIONS</span></div>
  <div class="row" style="top:216px"><div class="num">01</div><div class="q">LOREM IPSUM DOLOR SIT AMET, CONSECTETUR ADIPISCING ELIT SED DO EIUSMOD ?</div><div class="pm">+</div></div>
  <div class="row" style="top:275px"><div class="num">02</div><div class="q">LOREM IPSUM DOLOR SIT AMET, CONSECTETUR ADIPISCING ELIT SED DO EIUSMOD ?</div><div class="pm">+</div></div>
  <div class="row open" style="top:333px"><div class="num">03</div><div class="q">LOREM IPSUM DOLOR SIT AMET, CONSECTETUR ADIPISCING ELIT SED DO EIUSMOD ?</div><div class="pm">-</div></div>
  <p class="answer">Lorem ipsum dolor sit amet, consectetur adipiscing elit, sed do eiusmod tempor incididunt ut labore et dolore magna aliqua. Ut enim ad minim veniam, quis nostrud exercitation ullamco laboris nisi ut aliquip ex ea commodo consequat. Duis aute irure dolor in reprehenderit in voluptate velit esse cillum dolore eu fugiat nulla pariatur. Excepteur sint occaecat cupidatat non proident, sunt in culpa qui officia deserunt mollit anim id est laborum.</p>
  <div class="row" style="top:498px"><div class="num">04</div><div class="q">LOREM IPSUM DOLOR SIT AMET, CONSECTETUR ADIPISCING ELIT SED DO EIUSMOD ?</div><div class="pm">+</div></div>
  <div class="row" style="top:557px"><div class="num">05</div><div class="q">LOREM IPSUM DOLOR SIT AMET, CONSECTETUR ADIPISCING ELIT SED DO EIUSMOD ?</div><div class="pm">+</div></div>
  <div class="row" style="top:615px"><div class="num">06</div><div class="q">LOREM IPSUM DOLOR SIT AMET, CONSECTETUR ADIPISCING ELIT SED DO EIUSMOD ?</div><div class="pm">+</div></div>
</section>

<section class="gallery">
  <div class="photo bg" role="img" aria-label="Faint tattoo machine in the background"></div>
  <div class="ghost-num" style="top:50px">04</div>
  <div class="section-title" style="top:118px">OUR <span class="gold">TATTOO GALLERY</span></div>
  <svg class="rule" style="left:474px;top:157px" width="250" height="10"><circle cx="5" cy="5" r="4.5" fill="#fff"/><path d="M5 4 L238 3.5 L250 4.5 L238 6.5 L5 6Z" fill="#fff"/></svg>

  <div class="tile photo" role="img" aria-label="Tattoo being inked on skin" style="left:160px;top:219px;width:214px;height:201px;background:linear-gradient(135deg,#5a4030,#c08a60 55%,#2a1d16)"></div>
  <div class="tile photo" role="img" aria-label="Artist tattooing with gloved hands" style="left:160px;top:426px;width:214px;height:202px;background:linear-gradient(135deg,#1e2a24,#4a5a50 50%,#141814)"></div>
  <div class="tile photo" role="img" aria-label="Gloved hand with tattoo machine over a mandala design" style="left:160px;top:634px;width:214px;height:275px;background:linear-gradient(150deg,#2a2a2a,#7a6a62 50%,#c9a596)"></div>

  <div class="tile photo" role="img" aria-label="Colour tattoo work close-up" style="left:382px;top:219px;width:214px;height:274px;background:linear-gradient(160deg,#1a1a1a,#7a4030 55%,#3a2420)"></div>
  <div class="tile photo" role="img" aria-label="Woman with back tattoo in a field" style="left:382px;top:499px;width:214px;height:202px;background:linear-gradient(180deg,#6a6270,#8a6a66 60%,#4a3e3a)"></div>
  <div class="tile photo" role="img" aria-label="Tattoo artist at work in the studio" style="left:382px;top:707px;width:214px;height:202px;background:linear-gradient(150deg,#5a5a5a,#2a2a2a 60%,#8a7a70)"></div>

  <div class="tile photo" role="img" aria-label="Black and white photo of tattoo machine in use" style="left:604px;top:219px;width:214px;height:201px;background:linear-gradient(135deg,#3a3a3a,#8a8a8a 50%,#1e1e1e)"></div>
  <div class="tile photo" role="img" aria-label="Artist tattooing under blue light" style="left:604px;top:426px;width:214px;height:202px;background:linear-gradient(135deg,#0e1a2e,#2a4a7a 50%,#6a5a40)"></div>
  <div class="tile photo" role="img" aria-label="Tattooed woman with purple hair" style="left:604px;top:634px;width:214px;height:275px;background:linear-gradient(150deg,#7a3aa0,#c8a8b8 50%,#6a6a72)"></div>

  <div class="tile photo" role="img" aria-label="Man with tattooed hands adjusting a bow tie" style="left:826px;top:219px;width:214px;height:274px;background:linear-gradient(170deg,#3a2e26,#2a2a30 50%,#5a4a40)"></div>
  <div class="tile photo" role="img" aria-label="Heavily tattooed man crouching" style="left:826px;top:499px;width:214px;height:202px;background:linear-gradient(160deg,#4a4a4a,#7a4a3a 50%,#2a2a2a)"></div>
  <div class="tile photo" role="img" aria-label="Tattoo being wrapped after session" style="left:826px;top:707px;width:214px;height:202px;background:linear-gradient(135deg,#8a6a2a,#c8a070 50%,#3a2a1a)"></div>
</section>

<section class="contact">
  <div class="photo" role="img" aria-label="Dark studio backdrop"></div>
  <div class="ghost-num" style="top:15px">05</div>
  <div class="section-title" style="top:94px">GET <span class="gold">IN TOUCH</span></div>
  <svg class="rule" style="left:474px;top:133px" width="250" height="10"><circle cx="5" cy="5" r="4.5" fill="#fff"/><path d="M5 4 L238 3.5 L250 4.5 L238 6.5 L5 6Z" fill="#fff"/></svg>

  <div class="field" style="left:185px;top:202px">First name</div>
  <div class="field" style="left:452px;top:202px">Last name</div>
  <div class="field" style="left:185px;top:251px">Email Address</div>
  <div class="field" style="left:452px;top:251px">Phone Number</div>
  <div class="field" style="left:185px;top:301px">What Tattoo ?</div>
  <div class="field" style="left:452px;top:301px;height:88px">Message</div>
  <div class="btn" style="left:185px;top:351px;width:256px;height:38px">SUBMIT NOW</div>

  <div class="info" style="top:203px"><div class="ico"><svg width="14" height="18" viewBox="0 0 14 18"><path d="M7 0C3 0 0 3 0 7c0 5 7 11 7 11s7-6 7-11c0-4-3-7-7-7z" fill="#fff"/><circle cx="7" cy="7" r="2.5" fill="#d4a00c"/></svg></div><div><h4>Location</h4><p>123 Lorem ipsum dolor sit amet cons<br>ectetur adipiscing elit.</p></div></div>
  <div class="info" style="top:282px"><div class="ico"><svg width="16" height="16" viewBox="0 0 24 24"><path d="M6.6 10.8a15 15 0 006.6 6.6l2.2-2.2a1 1 0 011-.25 11.4 11.4 0 003.6.57 1 1 0 011 1V20a1 1 0 01-1 1A17 17 0 013 4a1 1 0 011-1h3.5a1 1 0 011 1c0 1.25.2 2.45.57 3.6a1 1 0 01-.25 1z" fill="#fff"/></svg></div><div><h4>Phone Number</h4><p>+1 123 456 7890</p></div></div>
  <div class="info" style="top:356px"><div class="ico"><svg width="16" height="12" viewBox="0 0 16 12"><rect width="16" height="12" rx="1.5" fill="#fff"/><path d="M1 1l7 5 7-5" stroke="#d4a00c" fill="none" stroke-width="1.4"/></svg></div><div><h4>Email Address</h4><p>hello@gildedviper.studio</p></div></div>
</section>

<footer class="footer">
  <div class="foot-brand"><div class="dot"></div><span>THE GILDED<br>VIPER</span></div>

  <div class="fcol" style="left:287px"><h5><b>Quick</b> Links</h5>
    <ul><li><i>»</i>Home</li><li><i>»</i>About</li><li><i>»</i>FAQ</li><li><i>»</i>Gallery</li><li><i>»</i>Inquiries</li><li><i>»</i>Shop</li></ul></div>

  <div class="fcol" style="left:423px"><h5><b>Follow</b> Us</h5>
    <ul><li><span class="sq"></span>Studio Page</li><li><span class="sq"></span>Ink Journal</li><li><span class="sq"></span>Flash Sheets</li><li><span class="sq"></span>Studio Clips</li><li><span class="sq"></span>Artist Profile</li></ul></div>

  <div class="fcol" style="left:559px"><h5><b>Contact</b> Info</h5>
    <div class="fc-item"><div class="ico"><svg width="10" height="13" viewBox="0 0 14 18"><path d="M7 0C3 0 0 3 0 7c0 5 7 11 7 11s7-6 7-11c0-4-3-7-7-7z" fill="#fff"/><circle cx="7" cy="7" r="2.5" fill="#d4a00c"/></svg></div><div><h6>Location</h6><p>123 Lorem ipsum dolor sit<br>ectetur adipiscing elit.</p></div></div>
    <div class="fc-item"><div class="ico"><svg width="12" height="12" viewBox="0 0 24 24"><path d="M6.6 10.8a15 15 0 006.6 6.6l2.2-2.2a1 1 0 011-.25 11.4 11.4 0 003.6.57 1 1 0 011 1V20a1 1 0 01-1 1A17 17 0 013 4a1 1 0 011-1h3.5a1 1 0 011 1c0 1.25.2 2.45.57 3.6a1 1 0 01-.25 1z" fill="#fff"/></svg></div><div><h6>Phone Number</h6><p>+1 123 456 7890</p></div></div>
    <div class="fc-item" style="margin-top:22px"><div class="ico"><svg width="12" height="9" viewBox="0 0 16 12"><rect width="16" height="12" rx="1.5" fill="#fff"/><path d="M1 1l7 5 7-5" stroke="#d4a00c" fill="none" stroke-width="1.4"/></svg></div><div><h6>Email Address</h6><p>hello@gildedviper.studio</p></div></div>
  </div>

  <div class="fcol nl" style="left:782px"><h5><b>Our</b> Newsletter</h5>
    <p>Lorem ipsum dolor sit amet, consectetur adipiscing elitsed do eiusmod tempor incididunt ut</p>
    <div class="in">Enter The Name *</div>
    <div class="in">Enter The Email *</div>
    <div class="btn" style="position:relative;margin-top:24px;width:143px;height:31px">SUBSCRIBE NOW</div>
  </div>

  <div class="abs" style="left:152px;top:291px;width:896px;height:1px;background:#555"></div>
  <div class="abs" style="left:0;top:313px;width:1200px;text-align:center;font-size:11px">© copyrights 2023 <span class="gold">The Gilded Viper</span> &nbsp;|&nbsp;&nbsp; All rights reserved.</div>
</footer>

</div>
</body>
</html>
```